Lark and Fern: Prespective and Balence in People's Lives Needs a Buissness Card Design

Lark and Fern Community Center is an organization that seeks to bring balance into people's lives. Main services include: guided meditation, group brainstorming, and guided counseling. Lark and Fern combines Eastern practices, i.e. Buddhism, Hinduism, and Taoism, with Western practices: therapy, group brainstorming and healing. We would like a double sided card: 1) front vertical with image, 2) back horizontal with information. The main colors for the card are red, white, black. Different finishes would be nice--please no high gloss. Matte, pearlized, embossing--used tactfully and sparingly would be nice. The card should convey balance/harmony in a modern world.

```html
<!DOCTYPE html>
<html lang="en">
<head>
<meta charset="utf-8">
<title>Lark and Fern Community Center — Business Card</title>
<link rel="stylesheet" href="https://fonts.googleapis.com/css2?family=Bree+Serif&display=swap">
<style>
  :root {
    --ink: #0b0b0b;
    --paper: #ffffff;
    --signal: #e8212a;
    --stage: #e9e6e1;
    --card-font: "Bree Serif", Georgia, serif;
  }
  * { box-sizing: border-box; margin: 0; padding: 0; }
  html, body { width: 1200px; height: 900px; overflow: hidden; }
  body {
    background: var(--stage);
    font-family: var(--card-font);
    position: relative;
  }

  /* Front: vertical split card */
  .card-front {
    position: absolute;
    left: 110px; top: 170px;
    width: 340px; height: 560px;
    display: flex;
    box-shadow: 0 6px 18px rgba(0,0,0,.18);
    overflow: hidden;
  }
  .card-front .half-light { flex: 1; background: var(--paper); }
  .card-front .half-dark  { flex: 1; background: var(--ink); }
  .front-mark {
    position: absolute;
    left: 50%; top: 50%;
    transform: translate(-50%, -50%);
    display: flex; flex-direction: column; align-items: center; gap: 16px;
  }
  .front-mark .mark-dot {
    width: 150px; height: 150px; border-radius: 50%;
    background: var(--signal);
  }

  /* Back: horizontal info card */
  .card-back {
    position: absolute;
    left: 540px; top: 285px;
    width: 560px; height: 330px;
    background: var(--ink);
    color: var(--paper);
    box-shadow: 0 6px 18px rgba(0,0,0,.25);
    padding: 34px 38px;
  }
  .org-name {
    color: var(--signal);
    font-size: 25px;
    letter-spacing: .5px;
    text-transform: uppercase;
  }
  .tagline { font-size: 16px; margin-top: 4px; }
  .person { margin-top: 22px; font-size: 16px; }
  .person .person-name { color: var(--signal); text-transform: uppercase; font-size: 18px; margin-right: 10px; }
  .contact {
    margin-top: 14px;
    display: grid;
    grid-template-columns: 64px 16px 1fr;
    row-gap: 3px;
    font-size: 14px;
  }
  .contact dt { color: var(--signal); }
  .contact .sep { color: var(--signal); }
  .address { margin-top: 12px; font-size: 14px; line-height: 1.35; }

  .back-mark {
    position: absolute;
    right: 38px; bottom: 30px;
    display: flex; align-items: center; gap: 10px;
  }
  .back-mark .mark-dot {
    width: 46px; height: 46px; border-radius: 50%;
    background: var(--signal);
  }
  .mark-name { color: var(--paper); font-size: 18px; }
</style>
</head>
<body>

  <section class="card-front" aria-label="Card front">
    <div class="half-light"></div>
    <div class="half-dark"></div>
    <div class="front-mark">
      <span class="mark-dot"></span>
    </div>
  </section>

  <section class="card-back" aria-label="Card back">
    <h1 class="org-name">Lark and Fern Community Center</h1>
    <p class="tagline">Rejuvenating Meditation Techniques</p>
    <p class="person"><span class="person-name">Mara Quill</span>Manager</p>
    <dl class="contact">
      <dt>Phone</dt><span class="sep">:</span><dd>+100 555 0142</dd>
      <dt>E-Mail</dt><span class="sep">:</span><dd>maraquill@mail.com</dd>
      <dt>Web</dt><span class="sep">:</span><dd>www.larkandferncommunitycenter.org</dd>
      <dt>Blog</dt><span class="sep">:</span><dd>www.larkfernnotes.com</dd>
    </dl>
    <p class="address">14 Willow Row, Brookhaven<br>State, NY 10420</p>
    <div class="back-mark">
      <span class="mark-dot"></span>
      <span class="mark-name">Lark and Fern</span>
    </div>
  </section>

</body>
</html>
```